Album Jacket for young indie musicians in AFRICA #2 Baraka, Tumaini And Neema (Grace, Hope And Blessing)

We are ZEV SOUND (zev-sound.example), a music label for young African musicians living in a slum. I would like to ask you to design our new album's cover jacket. The title is Baraka, Tumaini And Neema (it means "Grace, Hope And Blessing" in Swahili. I entrust you whether you use English words in the design or not.), musician name is Jabari Okoth. Add our label logo (we have various versions and can provide). I attached Jabari Okoth's photo also. Please listen to the music of the album on Soundcloud. https://tunecove.example/tags/jabariokoth

Target Market(s)

International. not only African music funs.

Requirements
Must have
• Title, Musician's name, ZEV SOUND Logo
• In order to upload to iTunes, I require the final that the following conditions are met.
• 1400 x 1400 pixels
• JPG file type
• 72 - 300dpi (300dpi is the best)
• Less than 25mb
• RGB color scheme (not CMYK)
Nice to have
• His music is something bright and little funny. Please express the tone of music in the design.
Should not have
• African traditional image

```html
<!DOCTYPE html>
<html lang="en">
<head>
<meta charset="utf-8">
<title>Baraka, Tumaini And Neema — Jabari Okoth</title>
<link href="https://fonts.googleapis.com/css2?family=Arimo:wght@400;700&display=swap" rel="stylesheet">
<style>
  :root {
    --paper: #e8ebf1;
    --crimson: #c42048;
    --rose: #d9587c;
    --amber: #e9a83c;
    --sun: #f0cf3a;
    --blush: #e7a3b6;
    --ink: #0b0b0b;
  }
  html, body {
    margin: 0;
    padding: 0;
    width: 1200px;
    height: 1200px;
    overflow: hidden;
    background: var(--paper);
  }
  .cover {
    position: relative;
    width: 1200px;
    height: 1200px;
    overflow: hidden;
    font-family: "Arimo", Arial, sans-serif;
  }
  .cover__artwork {
    position: absolute;
    inset: 0;
    background:
      radial-gradient(ellipse 60% 22% at 70% 50%, rgba(240, 207, 58, 0.55), transparent 70%),
      radial-gradient(ellipse 55% 18% at 35% 72%, rgba(233, 168, 60, 0.6), transparent 70%),
      radial-gradient(ellipse 40% 20% at 70% 92%, rgba(231, 163, 182, 0.7), transparent 70%),
      linear-gradient(160deg,
        var(--paper) 0%,
        var(--paper) 24%,
        var(--crimson) 34%,
        var(--crimson) 44%,
        var(--amber) 58%,
        var(--rose) 74%,
        var(--crimson) 88%,
        var(--rose) 100%);
  }
  .cover__titles {
    position: absolute;
    left: 46px;
    top: 46px;
    color: var(--ink);
    font-weight: 400;
    font-size: 45px;
    line-height: 64px;
    letter-spacing: 0;
  }
  .cover__title,
  .cover__artist {
    margin: 0;
    font-size: inherit;
    font-weight: inherit;
  }
  .label-mark {
    position: absolute;
    left: 772px;
    top: 1082px;
    display: flex;
    align-items: center;
    gap: 14px;
    color: var(--ink);
  }
  .label-mark__dot {
    width: 40px;
    height: 40px;
    border-radius: 50%;
    background: var(--ink);
  }
  .label-mark__name {
    font-weight: 700;
    font-size: 42px;
    letter-spacing: 0.5px;
  }
</style>
</head>
<body>
  <main class="cover">
    <div class="cover__artwork" role="img" aria-label="Abstract painted sweep of crimson, yellow and orange strokes rising across pale paper"></div>

    <header class="cover__titles">
      <h1 class="cover__title">Baraka, Tumaini And Neema</h1>
      <h2 class="cover__artist">Jabari Okoth</h2>
    </header>

    <div class="label-mark">
      <span class="label-mark__dot"></span>
      <span class="label-mark__name">ZEV SOUND</span>
    </div>
  </main>
</body>
</html>
```